KTV Consulting

Government/Entitlement Consulting Services- I assist developers obtain entitlements from local, state and federal government agencies so that they can build their projects. Often these projects are very complicated and political and may face community opposition.

Target Market(s)

Real Estate Developers

Industry/Entity Type

Business Consultant

Contact Information for Business Card

Dana Pelletier
Principal

Font styles to use
Serif
Sans Serif

Requirements
Must have
• Classy and professional appeal.
Nice to have
• I like a combination of a mat and glossy finish. I've seen that done with black and then a bold color for a pop, but am not 100% committed to that.

```html
<!DOCTYPE html>
<html lang="en">
<head>
<meta charset="utf-8">
<title>KTV Consulting – Business Card</title>
<link href="https://fonts.googleapis.com/css2?family=Arimo:wght@400;700&display=swap" rel="stylesheet">
<style>
  :root {
    --stage: #1e1e1e;
    --card-white: #ffffff;
    --card-shade: #ececec;
    --ink: #111111;
    --panel: #3a3a3a;
    --panel-dark: #262626;
    --panel-line: #1a1a1a;
    --panel-text: #f2f2f2;
    --tab: #151515;
  }
  * { margin: 0; padding: 0; box-sizing: border-box; }
  html, body {
    width: 1200px; height: 922px; overflow: hidden;
    background: var(--stage);
    font-family: "Arimo", Arial, sans-serif;
  }
  .stage {
    position: relative; width: 1200px; height: 922px;
  }
  .card {
    position: absolute; left: 280px;
    width: 640px; height: 366px;
    border-radius: 16px; overflow: hidden;
    background: radial-gradient(ellipse at 45% 40%, var(--card-white) 55%, var(--card-shade) 100%);
    box-shadow: 0 10px 30px rgba(0,0,0,.5);
  }
  .card--front { top: 70px; }
  .card--back { top: 486px; }

  .front-name {
    position: absolute; inset: 0;
    display: flex; align-items: center; justify-content: center;
    font-size: 54px; font-weight: 700; color: var(--ink);
    letter-spacing: -0.5px;
  }
  .back-name {
    position: absolute; left: 0; top: 0; width: 360px; height: 100%;
    display: flex; align-items: center; justify-content: center;
    font-size: 31px; font-weight: 700; color: var(--ink);
    letter-spacing: -0.3px;
  }
  .contact-panel {
    position: absolute; left: 360px; top: 0; width: 280px; height: 100%;
    background: linear-gradient(135deg, var(--panel) 0%, var(--panel-dark) 100%);
    display: flex; flex-direction: column;
  }
  .contact-row {
    position: relative; flex: 1;
    border-bottom: 1px solid var(--panel-line);
    box-shadow: 0 1px 0 rgba(255,255,255,.06);
    padding-left: 36px;
    display: flex; flex-direction: column; justify-content: center;
    color: var(--panel-text); font-size: 14px; line-height: 1.45;
  }
  .contact-row:last-child { border-bottom: none; box-shadow: none; }
  .contact-icon {
    position: absolute; left: -20px; top: 50%; transform: translateY(-50%);
    width: 36px; height: 36px; border-radius: 5px;
    background: var(--tab);
    box-shadow: 0 2px 4px rgba(0,0,0,.5);
    display: flex; align-items: center; justify-content: center;
  }
  .contact-icon svg { width: 20px; height: 20px; fill: #fff; }
  .person-name { font-size: 21px; line-height: 1.1; }
  .person-role { font-size: 14px; }
</style>
</head>
<body>
<main class="stage">
  <section class="card card--front" aria-label="Card front">
    <div class="front-name">KTV Consulting</div>
  </section>

  <section class="card card--back" aria-label="Card back">
    <div class="back-name">KTV Consulting</div>
    <div class="contact-panel">
      <div class="contact-row">
        <span class="contact-icon"><svg viewBox="0 0 20 20"><circle cx="10" cy="6" r="4"/><path d="M2 19c0-5 3.5-7 8-7s8 2 8 7z"/></svg></span>
        <span class="person-name">Dana Pelletier</span>
        <span class="person-role">Principal</span>
      </div>
      <div class="contact-row">
        <span class="contact-icon"><svg viewBox="0 0 20 20"><path d="M2 8l8-6 8 6v10H2z"/><circle cx="10" cy="12" r="3" fill="none" stroke="#151515" stroke-width="1.6"/></svg></span>
        <span>www.ktvadvisory.com</span>
        <span>hello@ktvadvisory.com</span>
      </div>
      <div class="contact-row">
        <span class="contact-icon"><svg viewBox="0 0 20 20"><rect x="5" y="1" width="10" height="18" rx="2"/><rect x="7" y="3.5" width="6" height="5" fill="#151515"/><g fill="#151515"><rect x="7" y="10" width="1.6" height="1.6"/><rect x="9.2" y="10" width="1.6" height="1.6"/><rect x="11.4" y="10" width="1.6" height="1.6"/><rect x="7" y="13" width="1.6" height="1.6"/><rect x="9.2" y="13" width="1.6" height="1.6"/><rect x="11.4" y="13" width="1.6" height="1.6"/></g></svg></span>
        <span>555-214-0187</span>
      </div>
      <div class="contact-row">
        <span class="contact-icon"><svg viewBox="0 0 20 20"><path d="M10 2l9 8h-3v8h-4v-5H8v5H4v-8H1z"/></svg></span>
        <span>14 Harlow Lane Eastvale</span>
        <span>NSW 2190</span>
      </div>
    </div>
  </section>
</main>
</body>
</html>
```